We are looking for an effective ad to recruit work from home Loan Officers for our Mortgage Brokerage.
Use the following text...
Earn Mortgage Income in your sleep. Its as easy as 1, 2, 3.....
1) Solicit Potential Applicants (Word of Mouth, Email, Social Media etc.)
2) Take Complete Applications & Submit Them
3) Wait to Get Paid.......(Avg. $2,500 per closing)
"You open the door, we'll finish the deal"
No Experience Necessary
No Goals or Quotas
No Office Hours / Work from Home Office
...and We Fully Reimburse ALL LICENSING FEES!!
Email Resume to mwelby@brightharborloans.example
Bright Harbor Lending Group, Inc.
947 W Caldwell Avenue, #318
Baltimore, MD 21230
NMLS #731860
www.brightharborloans.example
Phone (800) 555-0142
Licensed Mortgage Broker in MD and DC since 1997
Target Market(s)
Professionals looking to earn part time income at Loan Officers, preferably with strong social media following.
Industry/Entity Type
Loan
Look and feel

```html
<!DOCTYPE html>
<html lang="en">
<head>
<meta charset="utf-8">
<title>Bright Harbor Lending Group – Loan Officer Recruitment</title>
<link href="https://fonts.googleapis.com/css2?family=Cinzel:wght@600;700&family=Oswald:wght@600&family=Lato:wght@400;700&display=swap" rel="stylesheet">
<style>
  :root{
    --gold:#c7b02b;
    --gold-light:#d9c53b;
    --gold-dark:#998a1f;
    --gold-text:#9d8d20;
    --blue:#1460a8;
    --blue-dark:#0d4f91;
    --ink:#111;
    --paper:#fff;
    --stage:#ebe8e2;
  }
  *{margin:0;padding:0;box-sizing:border-box}
  html,body{width:1200px;height:1200px;overflow:hidden;background:var(--stage)}
  .flyer{
    position:absolute;left:159px;top:29px;width:969px;height:1254px;
    transform:scale(.91);transform-origin:0 0;background:var(--paper);
    box-shadow:0 6px 24px rgba(0,0,0,.25);overflow:hidden;
    font-family:'Lato',sans-serif;
  }
  /* hero */
  .hero{position:absolute;left:0;top:0;width:969px;height:483px;
    background:linear-gradient(180deg,#fff 0%,#f1f1f1 100%)}
  .hero-photo{position:absolute;inset:0;
    background:linear-gradient(180deg,#6fa6e0 0%,#a9c9ec 28%,#b9a08a 45%,#8d7a68 60%,#5f8f3a 78%,#4d8a2a 100%);
    clip-path:polygon(525px 0,969px 0,969px 483px,410px 483px)}
  .hero-edge{position:absolute;inset:0}
  .brand{position:absolute;left:40px;top:70px;width:360px;display:flex;align-items:center;gap:14px}
  .brand-dot{width:46px;height:46px;border-radius:50%;background:var(--blue);flex:none}
  .brand-name{font-family:'Cinzel',serif;font-weight:700;font-size:25px;line-height:1.15;color:var(--blue)}
  .headline{position:absolute;left:30px;top:245px;width:385px;text-align:center;font-family:'Cinzel',serif;font-weight:700;line-height:1}
  .headline .l1{display:block;font-size:66px;color:var(--gold-text)}
  .headline .l2{display:block;font-size:56px;color:var(--blue);margin-top:4px}
  .headline .l3{display:block;font-size:25px;color:var(--gold-text);margin-top:10px;font-weight:600}
  /* perks band */
  .perks{position:absolute;left:0;top:490px;width:969px;height:187px;display:flex;
    background:var(--gold)}
  .perk{position:relative;height:100%;display:flex;flex-direction:column;align-items:center;padding-top:58px;
    background:linear-gradient(90deg,rgba(0,0,0,.04),rgba(255,255,255,.03) 50%,rgba(0,0,0,.06))}
  .perk:nth-child(1){width:292px}.perk:nth-child(2){width:438px}.perk:nth-child(3){width:239px}
  .perk-icon{width:56px;height:56px}
  .perk-label{margin-top:10px;font-size:18.5px;color:#1d1d1d}
  /* pitch */
  .pitch{position:absolute;left:0;top:677px;width:969px;height:494px;
    background:linear-gradient(180deg,#fff 0%,#f2f2f2 60%,#fff 100%)}
  .pitch-title{position:absolute;left:0;top:52px;width:969px;text-align:center;font-family:'Oswald',sans-serif;font-weight:600;font-size:54px;line-height:57px;color:var(--ink);letter-spacing:.5px}
  .pitch-title .accent{color:var(--blue)}
  .step{position:absolute;display:flex;align-items:center;height:54px;border-radius:0 16px 16px 0;
    font-weight:700;font-size:21px;padding-left:74px;box-shadow:4px 8px 8px -4px rgba(0,0,0,.25)}
  .step-num{position:absolute;left:-2px;top:50%;transform:translateY(-50%);width:64px;height:64px;border-radius:50%;
    display:flex;align-items:center;justify-content:center;font-size:38px;font-weight:700;border:3px solid #fff;box-shadow:0 0 0 2px var(--gold-dark)}
  .step.gold{background:linear-gradient(90deg,var(--gold),var(--gold-light));color:#111}
  .step.gold .step-num{background:var(--gold-light);color:#111}
  .step.blue{background:linear-gradient(90deg,var(--blue-dark),var(--blue));color:#fff}
  .step.blue .step-num{background:var(--blue);color:#fff;box-shadow:0 0 0 2px var(--blue-dark)}
  .s1{left:100px;top:253px;width:770px}
  .s2{left:218px;top:330px;width:534px}
  .s3{left:218px;top:410px;width:534px}
  /* footer */
  .footer{position:absolute;left:0;top:1171px;width:969px;height:83px}
  .footer-bg{position:absolute;left:0;top:0}
  .footer-text{position:absolute;font-size:14.5px;color:#1a1a1a;line-height:26px;white-space:nowrap}
  .footer-icon{flex:none;display:block}
  .addr{left:34px;top:14px}
  .addr .row{display:flex;align-items:center;gap:6px}
  .addr .indent{padding-left:24px}
  .nmls{left:549px;top:40px;color:#fff}
  .contact{left:728px;top:14px;color:#fff}
  .contact .row{display:flex;align-items:center;gap:8px}
</style>
</head>
<body>
<div class="flyer">
  <section class="hero">
    <div class="hero-photo" role="img" aria-label="Photo of a smiling young family sitting on the lawn in front of a large brick two-storey house"></div>
    <svg class="hero-edge" width="969" height="483" viewBox="0 0 969 483">
      <line x1="526" y1="0" x2="410" y2="483" stroke="#a3921f" stroke-width="4"/>
    </svg>
    <div class="brand">
      <span class="brand-dot"></span>
      <span class="brand-name">Bright Harbor Lending Group, Inc.</span>
    </div>
    <h1 class="headline">
      <span class="l1">YOU OPEN</span>
      <span class="l2">THE DOOR</span>
      <span class="l3">WE'LL FINISH THE DEAL</span>
    </h1>
  </section>

  <section class="perks">
    <div class="perk">
      <svg class="perk-icon" viewBox="0 0 56 56"><circle cx="28" cy="28" r="28" fill="var(--blue)"/><circle cx="28" cy="28" r="24" fill="none" stroke="#fff" stroke-width="1" opacity=".5"/><rect x="14" y="17" width="28" height="22" rx="2" fill="none" stroke="#fff" stroke-width="2"/><circle cx="21" cy="25" r="3" fill="#fff"/><path d="M16 34c1-4 9-4 10 0z" fill="#fff"/><path d="M29 24h9M29 28h9M29 32h7" stroke="#fff" stroke-width="2"/></svg>
      <span class="perk-label">No Experience Necessary</span>
    </div>
    <div class="perk">
      <svg class="perk-icon" viewBox="0 0 56 56"><circle cx="28" cy="28" r="28" fill="var(--blue)"/><circle cx="22" cy="20" r="6" fill="none" stroke="#fff" stroke-width="2"/><path d="M12 38c1-7 6-10 10-10" fill="none" stroke="#fff" stroke-width="2"/><circle cx="35" cy="35" r="9" fill="none" stroke="#fff" stroke-width="2"/><path d="M35 30v5h4" fill="none" stroke="#fff" stroke-width="2"/></svg>
      <span class="perk-label">No Office Hours / Work from Home Office</span>
    </div>
    <div class="perk">
      <svg class="perk-icon" viewBox="0 0 56 56"><circle cx="28" cy="28" r="28" fill="var(--blue)"/><circle cx="26" cy="30" r="14" fill="none" stroke="#fff" stroke-width="2"/><circle cx="26" cy="30" r="8" fill="none" stroke="#fff" stroke-width="2"/><circle cx="26" cy="30" r="2.5" fill="#fff"/><path d="M26 30L41 15M36 15h5v5" fill="none" stroke="#fff" stroke-width="2"/></svg>
      <span class="perk-label">No Goals or Quotas</span>
    </div>
  </section>

  <section class="pitch">
    <h2 class="pitch-title">EARN MORTGAGE INCOME<br><span class="accent">IN YOUR SLEEP</span><br>ITS AS EASY AS 1, 2, 3</h2>
    <div class="step gold s1"><span class="step-num">1</span>Solicit Potential Applicants (Word of Mouth, Email, Social Media etc.)</div>
    <div class="step blue s2"><span class="step-num">2</span>Take Complete Applications &amp; Submit Them</div>
    <div class="step gold s3"><span class="step-num">3</span>Wait to Get Paid.......(Avg. $2,500 per closing)</div>
  </section>

  <footer class="footer">
    <svg class="footer-bg" width="969" height="83" viewBox="0 0 969 83">
      <rect width="969" height="83" fill="var(--blue)"/>
      <polygon points="0,0 462,0 432,83 0,83" fill="var(--gold)"/>
      <polygon points="445,0 462,0 432,83 415,83" fill="var(--gold-dark)"/>
    </svg>
    <div class="footer-text addr">
      <div class="row"><svg class="footer-icon" width="18" height="22" viewBox="0 0 18 22"><path d="M9 1a7 7 0 0 0-7 7c0 5 7 13 7 13s7-8 7-13a7 7 0 0 0-7-7z" fill="#111"/><circle cx="9" cy="8" r="3" fill="var(--gold)"/></svg>947 W Caldwell Avenue, #318, Baltimore, MD 21230.</div>
      <div class="indent">Licensed Mortgage Broker in MD and DC since 1997</div>
    </div>
    <div class="footer-text nmls">NMLS #731860</div>
    <div class="footer-text contact">
      <div class="row"><svg class="footer-icon" width="20" height="16" viewBox="0 0 20 16"><rect x="1" y="1" width="5" height="14" rx="1" fill="none" stroke="#fff" stroke-width="1.5"/><rect x="7" y="3" width="12" height="12" rx="1" fill="none" stroke="#fff" stroke-width="1.5"/><path d="M10 7h2M14 7h2M10 10h2M14 10h2" stroke="#fff" stroke-width="1.5"/></svg>Phone (800) 555-0142</div>
      <div class="row"><svg class="footer-icon" width="20" height="20" viewBox="0 0 20 20"><circle cx="10" cy="10" r="8.5" fill="none" stroke="#fff" stroke-width="1.5"/><ellipse cx="10" cy="10" rx="4" ry="8.5" fill="none" stroke="#fff" stroke-width="1.5"/><path d="M2 10h16M3.5 6h13M3.5 14h13" stroke="#fff" stroke-width="1.2"/></svg>www.brightharborloans.example</div>
    </div>
  </footer>
</div>
</body>
</html>
```